Redesign of business card for Birchline Mechanical

We are looking for a new design for our business cards for Birchline Mechanical. We are a plumbing & HVAC construction company, operating on the West Coast of Canada and USA. Logo attached.
Industry/Entity Type
Construction - Plumbing & HVAC
Contact Information for Business Card
Name, address, phone numbers, email, website address
Look and feel
Each slider illustrates characteristics of the customer's brand and the style your logo design should communicate.

```html
<!DOCTYPE html>
<html lang="en">
<head>
<meta charset="utf-8">
<title>Birchline Mechanical – Business Card</title>
<link rel="stylesheet" href="https://fonts.googleapis.com/css2?family=Roboto:wght@300;400;500;700&display=swap">
<style>
  :root {
    --page: #ffffff;
    --card: #f1f1f1;
    --card-light: #f7f7f7;
    --card-shade: #e4e4e4;
    --ink: #070708;
    --text: #1c1c1e;
    --muted: #8a8a8c;
    --icon: #ffffff;
  }
  * { box-sizing: border-box; margin: 0; padding: 0; }
  html, body {
    width: 800px; height: 1200px; overflow: hidden;
    background: var(--page);
    font-family: "Roboto", Arial, sans-serif;
  }
  .sheet { position: relative; width: 800px; height: 1200px; }
  .card {
    position: absolute; left: 100px; width: 600px; height: 358px;
    overflow: hidden;
    box-shadow: 2px 3px 5px rgba(0,0,0,.28);
    background: var(--card);
  }
  .card--front { top: 222px; }
  .card--back { top: 620px; }
  .card__pattern {
    position: absolute; inset: 0;
    background: linear-gradient(135deg, var(--card-light) 0%, var(--card) 45%, var(--card-shade) 75%, var(--card-light) 100%);
  }
  .brand {
    position: absolute; display: flex; align-items: center; gap: 10px;
    color: var(--ink); font-weight: 700; white-space: nowrap;
  }
  .brand__square { background: var(--ink); flex: none; }
  .card--front .brand { left: 0; right: 0; top: 140px; justify-content: center; font-size: 34px; letter-spacing: .5px; }
  .card--front .brand__square { width: 30px; height: 30px; }
  .front__bar {
    position: absolute; left: 27.3%; width: 45.3%; bottom: 0; height: 40px;
    background: var(--ink);
  }
  .card--back .brand { left: 72px; top: 166px; font-size: 19px; }
  .card--back .brand__square { width: 18px; height: 18px; }
  .back__strip {
    position: absolute; left: 322px; top: 89px; bottom: 0; width: 39px;
    background: var(--ink);
  }
  .back__icon { position: absolute; left: 50%; transform: translateX(-50%); width: 15px; height: 15px; fill: var(--icon); }
  .contact { position: absolute; left: 374px; color: var(--text); }
  .contact__name { top: 112px; font-size: 23px; font-weight: 700; }
  .contact__role { top: 141px; font-size: 14px; font-weight: 300; color: var(--muted); }
  .contact__line { font-size: 14.5px; font-weight: 300; line-height: 19px; }
</style>
</head>
<body>
<main class="sheet">

  <section class="card card--front" aria-label="Card front">
    <div class="card__pattern" role="img" aria-label="Soft grey overlapping triangle pattern"></div>
    <div class="brand"><span class="brand__square"></span>Birchline Mechanical</div>
    <div class="front__bar"></div>
  </section>

  <section class="card card--back" aria-label="Card back">
    <div class="card__pattern" role="img" aria-label="Soft grey overlapping triangle pattern"></div>
    <div class="brand"><span class="brand__square"></span>Birchline Mechanical</div>

    <div class="back__strip">
      <svg class="back__icon" style="top:40px" viewBox="0 0 16 16" aria-hidden="true"><circle cx="8" cy="5" r="3.5"/><path d="M1.5 15c0-3.6 3-5.5 6.5-5.5s6.5 1.9 6.5 5.5z"/></svg>
      <svg class="back__icon" style="top:106px" viewBox="0 0 16 16" aria-hidden="true"><path d="M3.2 1l2.6 3.2-1.5 1.8c.9 2 2.6 3.7 4.6 4.6l1.8-1.5L14 11.8l-1.6 2.4C7 14.5 1.4 9 1.8 3.6z"/></svg>
      <svg class="back__icon" style="top:136px" viewBox="0 0 16 16" aria-hidden="true"><path d="M1 3h14v1.2L8 9 1 4.2z"/><path d="M1 5.8l7 4.8 7-4.8V13H1z"/></svg>
      <svg class="back__icon" style="top:166px" viewBox="0 0 16 16" aria-hidden="true"><g fill="none" stroke="#fff" stroke-width="1.2"><circle cx="8" cy="8" r="6.5"/><ellipse cx="8" cy="8" rx="3" ry="6.5"/><path d="M1.5 8h13M2.5 4.8h11M2.5 11.2h11"/></g></svg>
      <svg class="back__icon" style="top:197px" viewBox="0 0 16 16" aria-hidden="true"><path d="M8 0.8a5 5 0 0 0-5 5c0 3.6 5 9.4 5 9.4s5-5.8 5-9.4a5 5 0 0 0-5-5zm0 7a2 2 0 1 1 0-4 2 2 0 0 1 0 4z"/></svg>
    </div>

    <p class="contact contact__name">Lorem Ipsum</p>
    <p class="contact contact__role">Lorem Ipsum</p>
    <p class="contact contact__line" style="top:192px">604-555-0182</p>
    <p class="contact contact__line" style="top:222px">info@birchlinemech.com</p>
    <p class="contact contact__line" style="top:253px">www.birchlinemech.com</p>
    <p class="contact contact__line" style="top:284px">4120 Harbour Lane,<br>Suite 200, Tacoma, WA 98402</p>
  </section>

</main>
</body>
</html>
```